An innovative software company needs a business card!

We need a business card design for our new innovative software company. Please use the details for the business card provided in business card details section. We will use the business card paper like: https://www.plavex.com/us/products/nfc/business-cards-plus.html Our company name: kelvora We have already a logo and colors to use in business cards too ,

Target Market(s)

App & Sofware Development

Industry/Entity Type

Software

Contact Information for Business Card

Lukas Brenner, BSc.
Owner and Creative Superhero

Adress:
Tulpenweg 37/4/1809
A - 4020, Linz

Tel: +43 (0) 676 921 35 60
Email: lukas.brenner@kelvora.at
Web: www.kelvora.at

Requirements
Must have
• - Use our logo
Nice to have
• It would be nice to have a nice picture on the backside. (About apps, software, technicals or funy stuff) - Use our colors as in business card (optional)

```html
<!DOCTYPE html>
<html lang="en">
<head>
<meta charset="utf-8">
<title>kelvora – business card</title>
<link rel="stylesheet" href="https://fonts.googleapis.com/css2?family=Source+Sans+3:wght@400;600;700&display=swap">
<style>
  :root {
    --backdrop: #000000;
    --card: #313235;
    --brand-blue: #1fa6d1;
    --text-light: #f1f1f1;
    --divider: #3c3d41;
  }
  * { margin: 0; padding: 0; box-sizing: border-box; }
  html, body {
    width: 1200px; height: 900px; overflow: hidden;
    background: var(--backdrop);
    font-family: "Source Sans 3", "Myriad Pro", Arial, sans-serif;
  }
  .stage { position: relative; width: 1200px; height: 900px; }
  .card {
    position: absolute; top: 271px;
    width: 457px; height: 281px;
    background: var(--card);
    border-radius: 14px;
  }
  .card--front { left: 137px; }
  .card--back { left: 626px; }

  .brand { position: absolute; display: flex; align-items: center; color: var(--brand-blue); font-weight: 700; }
  .brand__dot { display: block; border-radius: 50%; background: var(--brand-blue); }
  .card--front .brand { left: 48px; top: 116px; font-size: 30px; gap: 10px; }
  .card--front .brand__dot { width: 24px; height: 24px; }
  .card--back .brand { left: 84px; top: 98px; font-size: 64px; gap: 16px; letter-spacing: 1px; }
  .card--back .brand__dot { width: 42px; height: 42px; }

  .divider {
    position: absolute; left: 209px; top: 78px;
    width: 1px; height: 112px; background: var(--divider);
  }
  .contact { position: absolute; left: 248px; top: 60px; color: var(--text-light); font-size: 13.5px; line-height: 18px; }
  .contact__name { color: var(--brand-blue); font-size: 17px; font-weight: 600; line-height: 20px; }
  .contact__degree { font-size: 11px; }
  .contact__role { margin-bottom: 14px; }
  .contact__address { margin-bottom: 8px; }
  .contact__line { display: flex; align-items: center; gap: 6px; line-height: 19px; }
  .contact__icon { width: 10px; height: 10px; fill: var(--brand-blue); flex: none; }
</style>
</head>
<body>
<main class="stage">
  <section class="card card--front">
    <div class="brand"><span class="brand__dot"></span>kelvora</div>
    <div class="divider"></div>
    <div class="contact">
      <p class="contact__name">Lukas Brenner, <span class="contact__degree">BSc.</span></p>
      <p class="contact__role">Owner and Creative Superhero</p>
      <p class="contact__address">Tulpenweg 37/4/1809<br>A - 4020, Linz</p>
      <p class="contact__line">
        <svg class="contact__icon" viewBox="0 0 10 10" aria-hidden="true"><path d="M2 0.5l1.6 2.2-1 1c.6 1.3 1.5 2.2 2.8 2.8l1-1L8.6 7 8 9C4 9 1 6 1 1.6z"/></svg>
        +43 (0) 676 921 35 60
      </p>
      <p class="contact__line">
        <svg class="contact__icon" viewBox="0 0 10 10" aria-hidden="true"><path d="M0.5 2h9v6h-9z M0.5 2l4.5 3.4L9.5 2" stroke="#313235" stroke-width="0.8"/></svg>
        lukas.brenner@kelvora.at
      </p>
      <p class="contact__line">
        <svg class="contact__icon" viewBox="0 0 10 10" aria-hidden="true"><circle cx="5" cy="5" r="4.6"/><path d="M1 5h8M5 0.5c-2 2.5-2 6.5 0 9M5 0.5c2 2.5 2 6.5 0 9" stroke="#313235" stroke-width="0.7" fill="none"/></svg>
        www.kelvora.at
      </p>
    </div>
  </section>
  <section class="card card--back">
    <div class="brand"><span class="brand__dot"></span>kelvora</div>
  </section>
</main>
</body>
</html>
```